Generative AI radar Infographics

I want to create an infographic called "Automated Reasoning Horizon Chart for Tender Replies". (see slide 3 of the PowerPoint file). I want to use it on social media (Pellocast and Website). I added 2 inspiration graphics in my brief (see slide 2 of the PowerPoint). I want to add my logo on the infographic. (I also uploaded my company logos). You can find model detailed instructions on slide 1 of the PowerPoint.
Target Market(s)
Business development and sales
Industry/Entity Type
I am a business consultant. I will be using this infographics on Pellocast and in my powerpoint presentations to clients
Look and feel
Each slider illustrates characteristics of the customer's brand and the style your logo design should communicate.

```html
<!DOCTYPE html>
<html lang="en">
<head>
<meta charset="utf-8">
<title>Automated Reasoning Horizon Chart for Tender Replies</title>
<link rel="stylesheet" href="https://fonts.googleapis.com/css2?family=Cinzel:wght@600;700&family=Open+Sans:wght@400;700&display=swap">
<style>
  :root {
    --navy: #0b2e40;
    --teal: #0c93b8;
    --white: #ffffff;
  }
  html, body {
    margin: 0;
    padding: 0;
    overflow: hidden;
    background: var(--white);
  }
  .canvas {
    position: relative;
    width: 1200px;
    height: 1200px;
    overflow: hidden;
    background: var(--white);
  }
  .headline {
    position: absolute;
    left: 0;
    width: 1200px;
    margin: 0;
    text-align: center;
    font-family: "Cinzel", serif;
    font-weight: 700;
    line-height: 1;
  }
  .headline-main {
    top: 128px;
    font-size: 45px;
    color: var(--navy);
  }
  .headline-sub {
    top: 181px;
    font-size: 44px;
    color: var(--teal);
  }
  .radar {
    position: absolute;
    left: 0;
    top: 0;
  }
  .axis-label {
    font-family: "Cinzel", serif;
    font-weight: 700;
    fill: var(--teal);
  }
  .axis-label .big { font-size: 26px; }
  .axis-label .small { font-size: 18px; }
  .ring-label {
    font-family: "Open Sans", sans-serif;
    font-weight: 700;
    font-size: 26px;
    fill: var(--white);
    letter-spacing: 0.5px;
  }
  .item {
    font-family: "Open Sans", sans-serif;
    font-size: 11px;
  }
  .item-dark { fill: var(--navy); }
  .item-light { fill: var(--white); }
  .brand {
    position: absolute;
    left: 840px;
    top: 1104px;
    display: flex;
    align-items: center;
    gap: 10px;
    font-family: "Open Sans", sans-serif;
    font-weight: 700;
    font-size: 20px;
    color: var(--navy);
  }
  .brand-mark {
    width: 14px;
    height: 14px;
    background: var(--teal);
  }
</style>
</head>
<body>
<div class="canvas">
  <h1 class="headline headline-main">AUTOMATED REASONING HORIZON CHART</h1>
  <h2 class="headline headline-sub">FOR TENDER REPLIES</h2>

  <svg class="radar" width="1200" height="1200" viewBox="0 0 1200 1200">
    <defs>
      <path id="arc-tl" d="M348,676 A253,253 0 0 1 601,423"/>
      <path id="arc-tr" d="M601,423 A253,253 0 0 1 854,676"/>
      <path id="arc-bl" d="M328,676 A273,273 0 0 0 601,949"/>
      <path id="arc-br" d="M601,949 A273,273 0 0 0 874,676"/>
    </defs>

    <circle class="ring-outer" cx="601" cy="676" r="294" fill="var(--navy)"/>
    <circle class="ring-accent" cx="601" cy="676" r="233" fill="var(--teal)"/>
    <circle class="disc" cx="601" cy="676" r="225" fill="var(--white)"/>
    <path class="quadrant quadrant-tr" d="M605,672 L605,459 A217,217 0 0 1 818,672 Z" fill="var(--teal)"/>
    <path class="quadrant quadrant-bl" d="M597,680 L597,893 A217,217 0 0 1 384,680 Z" fill="var(--teal)"/>

    <g class="axes" fill="var(--teal)" stroke="none">
      <rect x="598.5" y="405" width="5" height="542"/>
      <rect x="330" y="673.5" width="542" height="5"/>
      <polygon points="601,383 582,416 620,416"/>
      <polygon points="601,970 582,937 620,937"/>
      <polygon points="307,676 340,657 340,695"/>
      <polygon points="895,676 862,657 862,695"/>
    </g>

    <circle class="hub" cx="601" cy="676" r="14" fill="var(--navy)"/>

    <text class="ring-label"><textPath href="#arc-tl" startOffset="50%" text-anchor="middle">DECISION SUPPORT</textPath></text>
    <text class="ring-label"><textPath href="#arc-tr" startOffset="50%" text-anchor="middle">PROPOSAL DEVELOPMENT</textPath></text>
    <text class="ring-label"><textPath href="#arc-bl" startOffset="50%" text-anchor="middle">CAPTURE STRATEGY</textPath></text>
    <text class="ring-label"><textPath href="#arc-br" startOffset="50%" text-anchor="middle">PROPOSAL STRATEGY</textPath></text>

    <g class="item item-dark" text-anchor="end">
      <text x="584" y="553">BID/NO BID ANALYSIS</text>
      <text x="584" y="571">BID QUALIFICATION</text>
      <text x="584" y="589">OPPORTUNITY ASSESSMENT</text>
      <text x="584" y="606">WIN PROBABILITY MODELING</text>
      <text x="584" y="624">STRATEGIC PRICING OPTIMIZATION</text>
      <text x="584" y="641">COMPLIANCE ASSESSMENT</text>
    </g>
    <g class="item item-light">
      <text x="623" y="520">COMPANY PROFILE</text>
      <text x="623" y="535">CV AND RESUMES</text>
      <text x="623" y="550">PAST PERFORMANCE</text>
      <text x="623" y="565">TECHNICAL SOLUTION</text>
      <text x="623" y="580">COMPLIANCE MATRIX</text>
      <text x="623" y="595">STATEMENT OF WORK</text>
      <text x="623" y="610">EXECUTIVE SUMMARY</text>
      <text x="623" y="625">SECURITY QUESTIONNAIRES</text>
      <text x="623" y="641">DUE DILIGENCE QUESTIONNAIRES</text>
    </g>
    <g class="item item-light" text-anchor="end">
      <text x="584" y="726">CAPTURE PLAN</text>
      <text x="584" y="745">SWOT ANALYSIS</text>
      <text x="584" y="764">CUSTOMER HOT BUTTONS</text>
      <text x="584" y="784">CUSTOMER INTELLIGENCE</text>
      <text x="584" y="803">COMPETITIVE INTELLIGENCE</text>
      <text x="584" y="822">VALUE PROPOSITION</text>
    </g>
    <g class="item item-dark">
      <text x="623" y="726">PROPOSAL PLAN</text>
      <text x="623" y="745">PROPOSAL OUTLINE</text>
      <text x="623" y="764">DIFFERENTIATORS</text>
      <text x="623" y="784">WIN THEME EXTRACTION</text>
      <text x="623" y="803">KEY MESSAGES EXTRACTION</text>
    </g>

    <g class="axis-label" text-anchor="middle">
      <text x="601" y="330" class="big">Process</text>
      <text x="601" y="355" class="big">Enhancement</text>
      <text x="601" y="1017" class="big">Strategy</text>
      <text x="601" y="1042" class="big">Enablement</text>
    </g>
    <g class="axis-label" text-anchor="end">
      <text x="280" y="654" class="big">Insights</text>
      <text x="280" y="679" class="big">Generation</text>
      <text x="280" y="699" class="small">(Transformative</text>
      <text x="280" y="719" class="small">application)</text>
    </g>
    <g class="axis-label">
      <text x="922" y="664" class="big">Task</text>
      <text x="922" y="689" class="big">Automation</text>
      <text x="922" y="709" class="small">(Foundational Use)</text>
    </g>
  </svg>

  <div class="brand">
    <span class="brand-mark"></span>
    <span class="brand-name">Kestrel Advisory Group</span>
  </div>
</div>
</body>
</html>
```